Business Card Design Project for Investment Fund

Orvanel Asset Partners is an emerging wealth management firm based in New Jersey. It offers superior investment returns to high net worth individuals and institutions by finding undervalued assets.
We recently selected a company logo which was inspired by the Tucana constellation. Beta Tucanae is a group of six stars, containing star cluster 47 Tucanae, rated the second brightest object in the sky.
Now we need a business card design. Since we are an investment firm, the design should project a sense of stability, growth and professionalism. The owner is interested in something simple yet striking, which of course is consistent with the logo.
Target Market(s)
Wealthy individuals, probably middle aged or older, in the US
Industry/Entity Type
Investment

```html
<!DOCTYPE html>
<html lang="en">
<head>
<meta charset="utf-8">
<title>Orvanel Asset Partners – Business Card</title>
<link rel="stylesheet" href="https://fonts.googleapis.com/css2?family=Montserrat:wght@600&family=Questrial&family=Roboto+Condensed:wght@400&display=swap">
<style>
  :root {
    --ink-dark: #2c373d;
    --ink-body: #1e1e1e;
    --band-navy: #1b2068;
    --band-text: #d9dce8;
    --mark-light: #2455cf;
    --mark-deep: #0c1a78;
    --divider: #8a8a8a;
    --paper-white: #ffffff;
    --paper-grey: #b5b6b9;
    --paper-soft: #d3d4d6;
  }
  * { margin: 0; padding: 0; box-sizing: border-box; }
  html, body { width: 1200px; height: 686px; overflow: hidden; background: var(--paper-white); }
  .card {
    position: relative;
    width: 1200px;
    height: 686px;
    overflow: hidden;
    background:
      radial-gradient(ellipse 75% 85% at 55% 45%, var(--paper-white) 35%, rgba(255,255,255,0) 100%),
      linear-gradient(110deg, var(--paper-grey) 0%, var(--paper-white) 45%, var(--paper-white) 70%, var(--paper-soft) 100%);
  }
  .brand-mark {
    position: absolute;
    left: 500px;
    top: 53px;
    width: 200px;
    height: 198px;
  }
  .brand-name {
    position: absolute;
    left: 0;
    right: 0;
    top: 282px;
    text-align: center;
    font-family: "Montserrat", sans-serif;
    font-weight: 600;
    font-size: 42px;
    letter-spacing: 0.09em;
    color: var(--ink-dark);
    text-transform: uppercase;
  }
  .holder {
    position: absolute;
    left: 100px;
    top: 442px;
    font-family: "Questrial", sans-serif;
    color: var(--ink-body);
  }
  .holder-name { font-size: 62px; line-height: 1; }
  .holder-title { font-size: 52px; line-height: 1; margin-top: 16px; }
  .divider {
    position: absolute;
    left: 566px;
    top: 440px;
    height: 146px;
    border-left: 2px dotted var(--divider);
  }
  .contact {
    position: absolute;
    left: 594px;
    top: 438px;
    font-family: "Roboto Condensed", sans-serif;
    font-size: 40px;
    line-height: 52px;
    color: var(--ink-body);
    list-style: none;
  }
  .web-band {
    position: absolute;
    left: 0;
    bottom: 0;
    width: 100%;
    height: 82px;
    background: var(--band-navy);
    display: flex;
    align-items: center;
    justify-content: center;
    font-family: "Roboto Condensed", sans-serif;
    font-size: 38px;
    color: var(--band-text);
  }
</style>
</head>
<body>
  <div class="card">
    <svg class="brand-mark" viewBox="0 0 200 198" aria-hidden="true">
      <defs>
        <linearGradient id="markFill" x1="0" y1="0" x2="1" y2="1">
          <stop offset="0" stop-color="var(--mark-light)"/>
          <stop offset="1" stop-color="var(--mark-deep)"/>
        </linearGradient>
      </defs>
      <rect x="0" y="0" width="200" height="198" rx="24" fill="url(#markFill)"/>
    </svg>

    <div class="brand-name">Orvanel Asset Partners</div>

    <div class="holder">
      <div class="holder-name">Julian Marlowe</div>
      <div class="holder-title">CEO</div>
    </div>

    <div class="divider"></div>

    <ul class="contact">
      <li>48 Harbor Ave.</li>
      <li>Newark, NJ 07102</li>
      <li>jmarlowe@orvanelasset.com</li>
    </ul>

    <div class="web-band">www.orvanelasset.com</div>
  </div>
</body>
</html>
```